letterhead design

We have a business card with logo, ink etc and want to develop letterhead that uses the elements of the business card logo.
Must haves...and they should be designed in, not just plopped in :)
Dr. Lyle Varden
2817 W Marlow Street
Fresno, CA 93614
559-382-6157 p
559-382-7043 f
info@brindlespine.com
www.brindlespine.com
www.facebook.com/brindlespn
Updates

Rather than just have the logo on the page, is there someway to silkscreen it in the background to fill the page?

Reason: I was out of town for a week.

Industry/Entity Type

Business

Requirements
Nice to have
• I'd like the logo somehow silk screened in the background of the paper as well.

```html
<!DOCTYPE html>
<html lang="en">
<head>
<meta charset="utf-8">
<title>Brindle Spine Letterhead</title>
<link rel="stylesheet" href="https://fonts.googleapis.com/css2?family=Open+Sans:wght@400;600;700&family=Parisienne&display=swap">
<style>
  :root {
    --backdrop: #e4e2df;
    --paper-top: #e2e2e2;
    --paper-bottom: #ffffff;
    --ink: #2b2b2b;
    --ink-soft: #555555;
    --signature: #7a7a7a;
    --band: #0c0c0c;
    --band-text: #ffffff;
    --mark: rgba(0, 0, 0, 0.045);
  }
  * { box-sizing: border-box; margin: 0; padding: 0; }
  html, body { width: 1200px; height: 1024px; overflow: hidden; }
  body {
    background: var(--backdrop);
    font-family: "Open Sans", Arial, sans-serif;
    color: var(--ink);
    position: relative;
  }
  .letterhead {
    position: absolute;
    left: 229px;
    top: 32px;
    width: 742px;
    height: 960px;
    background: linear-gradient(180deg, var(--paper-top) 0%, var(--paper-bottom) 55%, #f4f4f4 100%);
    box-shadow: 0 6px 24px rgba(0,0,0,0.25);
    overflow: hidden;
  }
  .background-mark {
    position: absolute;
    left: 120px;
    top: 330px;
    width: 520px;
    height: 300px;
    border-radius: 50%;
    background: radial-gradient(ellipse at center, var(--mark) 0%, rgba(0,0,0,0.02) 55%, rgba(0,0,0,0) 75%);
  }
  .brand {
    position: absolute;
    right: 56px;
    top: 52px;
    display: flex;
    align-items: center;
    gap: 10px;
  }
  .brand-square {
    width: 22px;
    height: 22px;
    background: var(--ink);
  }
  .brand-name {
    font-size: 30px;
    font-weight: 700;
    color: var(--ink);
    letter-spacing: 0.5px;
  }
  .letter-body {
    position: absolute;
    left: 60px;
    top: 150px;
    width: 600px;
    font-size: 11.5px;
    line-height: 1.45;
    color: var(--ink-soft);
  }
  .salutation { margin-bottom: 14px; font-size: 12.5px; }
  .letter-body p { margin-bottom: 12px; }
  .sign-off {
    position: absolute;
    left: 60px;
    top: 570px;
    z-index: 2;
  }
  .signature {
    font-family: "Parisienne", cursive;
    font-size: 28px;
    line-height: 1.3;
    color: var(--signature);
  }
  .sign-title {
    font-size: 12.5px;
    color: var(--ink-soft);
    margin-top: 2px;
  }
  .contact {
    position: absolute;
    right: 56px;
    top: 672px;
    text-align: right;
    font-size: 11.5px;
    line-height: 1.5;
    color: var(--ink);
    z-index: 2;
  }
  .contact li { list-style: none; display: flex; justify-content: flex-end; align-items: center; gap: 6px; }
  .contact svg { width: 11px; height: 11px; fill: var(--ink); flex: none; }
  .footer-band {
    position: absolute;
    left: 0;
    bottom: 0;
    width: 742px;
    height: 300px;
  }
  .footer-web {
    position: absolute;
    left: 58px;
    bottom: 36px;
    font-size: 14px;
    color: var(--band-text);
    letter-spacing: 0.3px;
    z-index: 2;
  }
</style>
</head>
<body>
<main class="letterhead">
  <div class="background-mark" role="img" aria-label="Faint screened brand mark filling the page background"></div>

  <header class="brand">
    <span class="brand-square"></span>
    <span class="brand-name">Brindle Spine</span>
  </header>

  <section class="letter-body">
    <p class="salutation">Lorem ipsum,</p>
    <p>Duis sit amet dolor sit amet dolor tempor iaculis ac nec ante. Proin nunc diam, egestas eu semper a, fermentum ac leo. Fusce sit amet tempor elit. Mauris auctor interdum massa vitae cursus. Ut adipiscing pellentesque nunc eget tincidunt magna imperdiet non. Curabitur eleifend elementum nisi eget iaculis. Suspendisse scelerisque ligula a nunc faucibus sit amet elementum dolor dictum.</p>
    <p>Praesent condimentum mi at ultrices fermentum, ipsum lectus consequat mauris, ut vulputate nibh erat id eros. Vivamus ornare mattis libero at dictum. Praesent sodales metus sed nulla laoreet mollis. Curabitur non turpis in orci dignissim gravida. Aliquam tristique mauris a nibh vestibulum sagittis.</p>
    <p>Duis porta semper nibh, tincidunt aliquam metus euismod eget. Morbi varius varius pellentesque. Donec aliquam vulputate tortor non hendrerit. Suspendisse at ipsum ante, interdum porttitor ligula. Curabitur eu molestie sapien. Sed magna purus, faucibus quis pulvinar nec, commodo vel justo. Nam faucibus ornare varius. Vivamus sit amet felis vitae justo scelerisque malesuada. Etiam venenatis vehicula magna, aceleifend lorem ornare nec. Maecenas eu nisi vel nunc aliquet malesuada vel in lacus.</p>
    <p>Morbi et odio eu ante pharetra iaculis vitae eget arcu. Maecenas gravida, dui vel ultricies aliquet, dui arcu luctus ante, non dignissim ipsum tortor vel orci, um fringilla mi. Mauris porta feugiat nibh et fermentum. Donec scelerisque consequat lacinia.</p>
    <p>Curabitur ac diam ut quam ultrices laoreet at ut tellus. Maecenas vitae urna in lorem condimentum sollicitudin eget vel lacus. Ut nisl turpis, tristique ullamcorper laoreet nec, gravida nec est. Donec elementum malesuada volutpat. In ac arcu quis augue vehicula fringilla.</p>
  </section>

  <div class="sign-off">
    <div class="signature">Dr. Lyle Varden</div>
    <div class="sign-title">Chiropractor</div>
  </div>

  <ul class="contact">
    <li>559-382-6157 <svg viewBox="0 0 12 12"><path d="M2.5 1h2l1 2.6-1.3 1a6 6 0 0 0 3.2 3.2l1-1.3 2.6 1v2a1 1 0 0 1-1 1A9.5 9.5 0 0 1 1.5 2a1 1 0 0 1 1-1z"/></svg></li>
    <li>559-382-7043 <svg viewBox="0 0 12 12"><rect x="3" y="1" width="6" height="3"/><rect x="1" y="4.5" width="10" height="4.5" rx="1"/><rect x="3" y="8" width="6" height="3"/></svg></li>
    <li>info@brindlespine.com <svg viewBox="0 0 12 12"><path d="M1 2.5h10v7H1z M1.6 3 6 6.4 10.4 3" fill="none" stroke="#2b2b2b" stroke-width="1.2"/></svg></li>
    <li>www.facebook.com/brindlespn <svg viewBox="0 0 12 12"><rect x="1" y="1" width="10" height="10" rx="1.5"/></svg></li>
    <li>2817 W Marlow Street, Fresno, CA 93614 <svg viewBox="0 0 12 12"><path d="M6 0.8a3.8 3.8 0 0 0-3.8 3.8C2.2 7.5 6 11.5 6 11.5s3.8-4 3.8-6.9A3.8 3.8 0 0 0 6 0.8zm0 5.3a1.5 1.5 0 1 1 0-3 1.5 1.5 0 0 1 0 3z"/></svg></li>
  </ul>

  <svg class="footer-band" viewBox="0 0 742 300" preserveAspectRatio="none" aria-hidden="true">
    <path d="M0 0 Q 430 90 742 290 L742 300 L0 300 Z" fill="var(--band)"/>
    <path d="M0 20 Q 420 108 742 316" fill="none" stroke="#ffffff" stroke-width="5"/>
  </svg>
  <div class="footer-web">www.brindlespine.com</div>
</main>
</body>
</html>
```